Veltrona Services

Double sided business cards with color on front and black and white on back. I have basic ideas and graphics, but am looking for someone to take them to the next level

```html
<!DOCTYPE html>
<html lang="en">
<head>
<meta charset="utf-8">
<title>Veltrona Services – Business Card</title>
<link rel="stylesheet" href="https://fonts.googleapis.com/css2?family=Poppins:wght@300;600&display=swap">
<style>
  :root {
    --backdrop: #c8c8c8;
    --card-dark: #0b0b0b;
    --card-light: #f1f1f1;
    --ink-light: #ffffff;
    --ink-dark: #0b0b0b;
    --card-shadow: rgba(0, 0, 0, 0.28);
  }
  * { box-sizing: border-box; margin: 0; padding: 0; }
  html, body {
    width: 1200px;
    height: 1005px;
    overflow: hidden;
    background: var(--backdrop);
    font-family: "Poppins", sans-serif;
  }
  .card {
    position: absolute;
    left: 320px;
    width: 560px;
    height: 320px;
    box-shadow: 0 14px 30px var(--card-shadow);
    overflow: hidden;
  }
  .card--front { top: 150px; background: var(--card-dark); color: var(--ink-light); }
  .card--back  { top: 535px; background: var(--card-light); color: var(--ink-dark); }
  .card__art { position: absolute; inset: 0; }
  .brand-mark {
    position: absolute;
    font-weight: 600;
    font-size: 15px;
    letter-spacing: 0.06em;
    text-transform: uppercase;
    text-align: center;
    width: 124px;
  }
  .card--front .brand-mark { left: 58px; top: 185px; color: var(--ink-dark); }
  .card--back .brand-mark  { left: 68px; top: 168px; color: var(--ink-dark); }
  .contact {
    position: absolute;
    left: 222px;
    top: 92px;
  }
  .contact__name {
    font-weight: 600;
    font-size: 19px;
    letter-spacing: 0.02em;
    text-transform: uppercase;
    line-height: 1.2;
  }
  .contact__phone {
    font-weight: 300;
    font-size: 40px;
    letter-spacing: 0.01em;
    line-height: 1.15;
  }
  .tagline {
    position: absolute;
    left: 232px;
    top: 112px;
    font-weight: 600;
    font-size: 17px;
    line-height: 1.25;
    text-transform: uppercase;
  }
</style>
</head>
<body>

  <section class="card card--front" aria-label="Card front">
    <svg class="card__art" width="560" height="320" viewBox="0 0 560 320" aria-hidden="true">
      <line x1="120" y1="0" x2="120" y2="132" stroke="#ffffff" stroke-width="3"/>
      <line x1="120" y1="264" x2="120" y2="320" stroke="#ffffff" stroke-width="3"/>
      <circle cx="120" cy="198" r="64" fill="#ffffff"/>
    </svg>
    <div class="brand-mark">Veltrona</div>
    <div class="contact">
      <p class="contact__name">Veltrona Services</p>
      <p class="contact__phone">555-014-2867</p>
    </div>
  </section>

  <section class="card card--back" aria-label="Card back">
    <svg class="card__art" width="560" height="320" viewBox="0 0 560 320" aria-hidden="true">
      <line x1="130" y1="0" x2="130" y2="110" stroke="#0b0b0b" stroke-width="3"/>
      <line x1="130" y1="250" x2="130" y2="320" stroke="#0b0b0b" stroke-width="3"/>
      <circle cx="130" cy="180" r="68" fill="none" stroke="#0b0b0b" stroke-width="3"/>
    </svg>
    <div class="brand-mark">Veltrona</div>
    <p class="tagline">A curated experience<br>all that is promised<br>is clarity</p>
  </section>

</body>
</html>
```